Need *Plum Crafted* Events Company Website
Bright Harbor Gatherings Website
Need *Plum Crafted* Events Company Website - Events
Creative Brief
Events
www.brightharborgatherings.example
Bright Harbor Gatherings (BHG) is a multi-dimensional event management firm providing all aspects of support and expertise for any special event. By providing upscale and individualized service, our events are unique and tailored around your personal vision, style and budget.
We provide partial and full-service event coordination services for all types of events; specializing in corporate meetings, conferences, receptions, and everyday social events.
We like unique and captivating web design that illustrates the characteristics of our brand and service offerrings. Our logo speaks to a company that is unique and classy with an edge. DISLIKE: Black or extremely dark backgrounds. Too fancy flash applications, Music or any kind of intro, anything that is too elaborate. LIKE: Easy flow and simplicity. I like the mix of soft neutrals
Feminine
neutral tones
pop of red
complementary tones
right side
www.vowlantern.example
www.quillaffairs.example
Will attached websites that we like later Please use the Fonts from my logo: Will attach files I would like for you to use the accent color on my logo as an special accent only so my logo is not overpowered. I am open to navigation placement but it does not give me that option so I selected what I believe is my personal preference.

```html
<!DOCTYPE html>
<html lang="en">
<head>
<meta charset="utf-8">
<title>Bright Harbor Gatherings</title>
<link href="https://fonts.googleapis.com/css2?family=Great+Vibes&family=Parisienne&family=Open+Sans:ital,wght@0,400;0,600;1,400&display=swap" rel="stylesheet">
<style>
  :root{
    --page-bg:#6f5159;
    --page-bg-deep:#5e434b;
    --panel:#4b3129;
    --panel-light:#5a3d33;
    --cream:#f0e7d9;
    --cream-deep:#e3d6c3;
    --stitch:#e9dcc9;
    --accent:#c8202b;
    --text-light:#eadfd2;
    --plum:#6d3e4c;
    --pink:#e6c7cc;
  }
  *{box-sizing:border-box;margin:0;padding:0}
  html,body{width:1200px;height:901px;overflow:hidden}
  body{
    position:relative;
    background:radial-gradient(circle at 50% 40%,var(--page-bg),var(--page-bg-deep));
    font-family:"Open Sans",Arial,sans-serif;
    color:var(--text-light);
  }
  .site{
    position:absolute;left:100px;top:0;width:1003px;height:901px;
    background:linear-gradient(180deg,var(--panel-light),var(--panel));
  }
  .site::before,.site::after{
    content:"";position:absolute;top:0;bottom:0;width:0;
    border-left:2px dashed var(--stitch);
  }
  .site::before{left:10px}
  .site::after{right:12px}
  .hero{
    position:absolute;left:34px;top:29px;width:650px;height:421px;
    border:6px solid #f4efe8;
    background:linear-gradient(160deg,#cbb9a3 0%,#9b8470 45%,#6b5546 100%);
  }
  .hero-tagline{
    position:absolute;left:0;right:0;top:118px;text-align:center;
    font-family:"Great Vibes",cursive;font-size:40px;color:#fff;letter-spacing:1px;
  }
  .thumbs{
    position:absolute;left:14px;right:14px;bottom:24px;height:108px;
    display:flex;gap:16px;
  }
  .thumb{flex:1;border:4px solid #f4efe8}
  .thumb.t1{background:linear-gradient(#8c98a6,#5c6574)}
  .thumb.t2{background:linear-gradient(#a99685,#5d4a3d)}
  .thumb.t3{background:linear-gradient(#6e5548,#3c2a22)}
  .thumb.t4{background:linear-gradient(#b0857f,#6b4a54)}
  .intro{position:absolute;left:40px;top:458px;width:650px}
  .intro h1{
    font-family:"Great Vibes",cursive;font-weight:400;font-size:30px;
    color:var(--text-light);margin-bottom:6px;
  }
  .intro p{font-size:11.5px;line-height:16px;color:var(--text-light);margin-bottom:14px}
  .player{
    position:absolute;left:39px;top:608px;width:255px;height:195px;
    background:linear-gradient(180deg,#fbeef0,var(--pink));
    border:2px solid #d8b9bf;
  }
  .player-brand{
    position:absolute;left:12px;top:46px;width:110px;text-align:center;
    font-family:"Great Vibes",cursive;font-size:22px;line-height:24px;color:var(--plum);
  }
  .player-bar{
    position:absolute;left:0;right:0;bottom:0;height:24px;background:#d9d9d9;
    border-top:1px solid #aaa;
  }
  .play{position:absolute;left:140px;top:36px}
  .testimonial{
    position:absolute;left:326px;top:620px;width:355px;height:183px;
    background:rgba(120,86,92,.55);
  }
  .testimonial h2{
    position:absolute;left:22px;top:-14px;padding:2px 14px;
    background:#8e7a77;
    font-family:"Great Vibes",cursive;font-weight:400;font-size:28px;color:#fff;
  }
  .quote-mark{
    position:absolute;left:22px;top:26px;font-family:Georgia,serif;
    font-size:120px;line-height:1;color:rgba(255,255,255,.18);
  }
  .testimonial blockquote{
    position:absolute;left:150px;top:42px;width:180px;
    font-size:11px;line-height:15px;font-style:italic;color:#f3e8e0;
  }
  .testimonial cite{
    position:absolute;right:22px;bottom:16px;font-size:10.5px;font-style:italic;color:#f3e8e0;
  }
  .footer{position:absolute;left:0;width:720px;top:845px;text-align:center;font-size:10.5px;line-height:19px;color:var(--text-light)}
  .footer a{color:var(--text-light);text-decoration:none}
  .sidebar{
    position:absolute;left:718px;top:0;width:254px;height:901px;
    background:linear-gradient(180deg,var(--cream),var(--cream-deep));
  }
  .brand{
    position:absolute;left:0;right:0;top:190px;text-align:center;
    font-family:"Great Vibes",cursive;font-size:30px;line-height:32px;color:var(--plum);
  }
  .brand-mark{
    display:block;width:14px;height:14px;border-radius:50%;background:var(--plum);
    margin:0 auto 10px;
  }
  .nav{position:absolute;left:0;right:0;top:445px;list-style:none;text-align:center}
  .nav li{height:40px;font-family:"Parisienne",cursive;font-size:21px;line-height:36px}
  .nav a{color:var(--accent);text-decoration:none}
  .connect{position:absolute;left:0;right:0;top:822px;text-align:center;font-size:12px;font-style:italic;color:#a49b90}
  .social{position:absolute;left:0;right:0;top:852px;display:flex;justify-content:center;gap:12px}
  .social span{width:22px;height:22px;background:#a8a198}
</style>
</head>
<body>
<div class="site">
  <div class="hero" role="img" aria-label="Photograph of an elegant banquet hall with chandelier and set tables">
    <div class="hero-tagline">Tailoring the finest events for you...</div>
    <div class="thumbs">
      <div class="thumb t1" role="img" aria-label="Photo of a conference audience"></div>
      <div class="thumb t2" role="img" aria-label="Photo of a business meeting"></div>
      <div class="thumb t3" role="img" aria-label="Photo of a dinner reception"></div>
      <div class="thumb t4" role="img" aria-label="Photo of a decorated celebration"></div>
    </div>
  </div>

  <section class="intro">
    <h1>Welcome to Bright Harbor Gatherings</h1>
    <p>Bright Harbor Gatherings (BHG) is a multi-dimensional event management firm providing all aspects of support and expertise for any special event. By providing upscale and individualized service, our events are unique and tailored around your personal vision, style and budget.</p>
    <p>We provide partial and full-service event coordination services for all types of events, specializing in corporate meetings, conferences, receptions, and everyday social events.</p>
  </section>

  <div class="player" aria-label="Video player">
    <div class="player-brand">Bright Harbor Gatherings</div>
    <svg class="play" width="76" height="76" viewBox="0 0 76 76">
      <circle cx="38" cy="38" r="34" fill="#f4dde0" stroke="#d6aeb5" stroke-width="3"/>
      <circle cx="38" cy="38" r="24" fill="#b88b93"/>
      <path d="M31 26 L52 38 L31 50 Z" fill="#fff"/>
    </svg>
    <svg class="player-bar" viewBox="0 0 251 24" preserveAspectRatio="none">
      <path d="M8 7 L16 12 L8 17 Z" fill="#555"/>
      <rect x="26" y="7" width="12" height="10" fill="#555"/>
      <rect x="48" y="8" width="12" height="8" fill="#555"/>
      <rect x="70" y="11" width="130" height="3" fill="#888"/>
      <circle cx="110" cy="12" r="5" fill="#666"/>
      <rect x="212" y="7" width="12" height="10" fill="none" stroke="#555" stroke-width="2"/>
      <rect x="232" y="7" width="12" height="10" fill="#555"/>
    </svg>
  </div>

  <section class="testimonial">
    <h2>Testimonials</h2>
    <div class="quote-mark">&ldquo;</div>
    <blockquote>Lorem ipsum dolor sit amet, consectetur adipiscing elit. Integer id magna purus, vel condimentum diam. Mauris libero dolor, hendrerit eget molestie gravida.</blockquote>
    <cite>~ Clara Whitmore</cite>
  </section>

  <footer class="footer">
    <div><a href="#">Home</a> | <a href="#">About us</a> | <a href="#">Services</a> | <a href="#">Contact us</a> | <a href="#">Events</a> | <a href="#">Our Blog</a></div>
    <div>Copyright &copy; 2011, Bright Harbor Gatherings. All rights reserved.</div>
  </footer>

  <aside class="sidebar">
    <div class="brand"><span class="brand-mark"></span>Bright Harbor<br>Gatherings</div>
    <ul class="nav">
      <li><a href="#">Home</a></li>
      <li><a href="#">About Us</a></li>
      <li><a href="#">Services</a></li>
      <li><a href="#">Contact Us</a></li>
      <li><a href="#">Events</a></li>
      <li><a href="#">Our Blog</a></li>
    </ul>
    <div class="connect">Connect with us</div>
    <div class="social">
      <span role="img" aria-label="Social network link"></span>
      <span role="img" aria-label="Social network link"></span>
      <span role="img" aria-label="Social network link"></span>
    </div>
  </aside>
</div>
</body>
</html>
```